Capestay Flyer

My business is as owner and manager of 6 holiday lets in the South West of WA in the wine region.
All our properties are on rural bush locations, but close to all the amenitiies of the Tarrabellup township and major wineries in the area.
we advertise all the properties thru lodgio.com.au
you can check out the details of all the properties with the following links
www.lodgio.com.au/55841 Wattles Retreat..Max occ 16
www.lodgio.com.au/61673 Emberlight Retreat Max occ 8
www.lodgio.com.au/66777 Quokkas Corner Max occ 12
www.lodgio.com.au/93104 Bellintary Max occ 10
www.lodgio.com.au/135790 The Glade Retreat Max occ 8
www.lodgio.com.au/147300 Ferncliff Studio Max Occ 4
i am looking to produce a flyer that i can leave in all the houses to promote one to the other.
**I would like the flyer to be DL size (pls ignore the A5 mentioned above).
DL (99 x 210 mm) - Please download the templates below:
Photoshop - http://printnook.com.au/propath/download-template.aspx?Log=1&path=propath&pfid=BFB&pf_id=BFB&type=2
Illustrator - http://printnook.com.au/propath/download-template.aspx?Log=1&path=propath&pfid=BFB&pf_id=BFB&type=3
Thanks for all the submissions, but we are happy with one designer and just about to compete the process.
Target Market(s)
Family groups on holidays
Industry/Entity Type
Business
Requirements
Must have
- Photos and descriptions of all the houses.
Must have a feel of holidays in the wine region
You can get from the links I have given .
Also must have the logo and personal details as used on the business card

```html
<!DOCTYPE html>
<html lang="en">
<head>
<meta charset="utf-8">
<title>Capestay DL Flyer</title>
<link href="https://fonts.googleapis.com/css2?family=Mulish:wght@400;600;700;800&display=swap" rel="stylesheet">
<style>
:root{
  --page:#e9e4dc;
  --paper:#ffffff;
  --ink:#2b2622;
  --body:#3d3833;
  --brown-dark:#3f332b;
  --brown-mid:#6a594c;
  --gold:#b3a552;
  --label:#f4f1ec;
}
*{box-sizing:border-box;margin:0;padding:0}
html,body{width:1200px;height:1000px;overflow:hidden}
body{background:var(--page);font-family:"Mulish",Arial,sans-serif;color:var(--ink);position:relative}

.flyer{position:absolute;background:var(--paper);box-shadow:0 2px 6px rgba(0,0,0,.18);overflow:hidden}
.flyer--front{left:148px;top:45px;width:458px;height:925px}
.flyer--back{left:608px;top:42px;width:436px;height:920px}

.photo{position:absolute}
.photo__label{position:absolute;background:var(--label);color:var(--ink);font-size:11px;padding:2px 6px;letter-spacing:.2px}

.brand{position:absolute;background:var(--paper);border-radius:50%;display:flex;flex-direction:column;align-items:center;justify-content:center;border:2px solid #ddd6cc}
.brand__name{font-weight:800;color:var(--ink);letter-spacing:1px;line-height:1}
.brand__tag{font-size:6.5px;color:var(--body);margin-top:3px;letter-spacing:.3px}

.contact-panel{position:absolute;left:0;top:710px;width:100%;height:215px;background:linear-gradient(160deg,var(--brown-mid),var(--brown-dark));color:#fff}
.property-list{position:absolute;left:58px;top:22px;width:200px}
.property-list__item{margin-bottom:5px}
.property-list__name{font-size:12px;font-weight:700;line-height:1.1}
.property-list__meta{font-size:10.5px;line-height:1.25;white-space:nowrap}
.property-list__meta a,.url{color:var(--gold);text-decoration:none}
.contacts{position:absolute;right:18px;top:14px;width:170px;text-align:right}
.contacts__brand{font-size:24px;line-height:26px;font-weight:800;color:#fff;letter-spacing:1px}
.contacts__tag{font-size:6px;line-height:8px;margin-bottom:4px}
.contacts__person{font-size:11.5px;line-height:14px;font-weight:700;margin-top:6px}
.contacts__phone{font-size:10px;line-height:12px;color:#fff}
.contacts__phone b,.contacts__email b{color:var(--gold);font-weight:600}
.contacts__email{position:absolute;right:18px;top:114px;font-size:9.5px;line-height:12px;white-space:nowrap;text-align:right}
.contacts__note{position:absolute;right:18px;top:134px;width:180px;font-size:9.8px;line-height:1.3;text-align:right}

.about{position:absolute;left:54px;top:198px;width:345px;height:640px;overflow:hidden}
.about__title{font-size:13px;font-weight:700;text-align:center;letter-spacing:.4px;margin:0 0 15px 18px}
.house{margin-bottom:9px}
.house__name{font-size:11px;font-weight:800;line-height:1.2}
.house__meta{font-size:9.6px;line-height:1.3;margin-bottom:2px}
.house__meta small{font-size:7px}
.house__text{font-size:9.6px;line-height:1.23;color:var(--body)}
.back-footer{position:absolute;left:0;bottom:0;width:100%;height:82px;background:var(--brown-mid);color:#fff;text-align:center;padding-top:10px}
.back-footer__note{font-size:9.6px}
.back-footer__brand{font-size:22px;font-weight:800;letter-spacing:1px;margin-top:10px}
</style>
</head>
<body>

<section class="flyer flyer--front">
  <div class="photo" style="left:2px;top:2px;width:254px;height:136px;background:linear-gradient(180deg,#5f6b3e,#4e6b2c 60%,#6f8a3a)" role="img" aria-label="Stone house among tall gum trees on a green lawn"></div>
  <span class="photo__label" style="left:22px;top:130px">Wattles Retreat</span>

  <div class="photo" style="left:264px;top:2px;width:180px;height:128px;background:linear-gradient(180deg,#3f4a44,#6a4a2d 70%,#8a5a36)" role="img" aria-label="Timber deck with outdoor table and chairs beside a dark clad house"></div>
  <span class="photo__label" style="left:334px;top:116px">The Glade Retreat</span>

  <div class="photo" style="left:6px;top:144px;width:290px;height:196px;background:linear-gradient(180deg,#8a5d36,#c9a682 45%,#dcd4c8)" role="img" aria-label="Open-plan living room with timber cathedral ceiling and white sofas"></div>
  <span class="photo__label" style="left:148px;top:144px">Ferncliff Studio</span>

  <div class="photo" style="left:302px;top:140px;width:152px;height:200px;background:linear-gradient(180deg,#4c6a3a,#7a8c5a 50%,#b3a58a)" role="img" aria-label="Covered verandah post looking out over bushland"></div>

  <div class="photo" style="left:18px;top:350px;width:164px;height:200px;background:linear-gradient(180deg,#e7e3df,#b9b1a8 55%,#5a5550)" role="img" aria-label="Bedroom with dark timber bed, white linen and bedside lamps"></div>

  <div class="photo" style="left:190px;top:346px;width:266px;height:200px;background:linear-gradient(180deg,#4f8fd0,#a7c6df 35%,#8a7a5a 60%,#3f7a2a)" role="img" aria-label="Timber cottage under blue sky with green lawn and gum tree"></div>
  <span class="photo__label" style="left:350px;top:520px">Quokkas Corner</span>

  <div class="photo" style="left:28px;top:556px;width:204px;height:152px;background:linear-gradient(180deg,#d8dde0,#6a7a5a 45%,#4a7a2a)" role="img" aria-label="Brick house with wraparound verandah and lawn"></div>
  <span class="photo__label" style="left:58px;top:694px">Emberlight Retreat</span>

  <div class="photo" style="left:238px;top:550px;width:218px;height:158px;background:linear-gradient(180deg,#6a6a5a,#a08060 50%,#8a4a34)" role="img" aria-label="Brick house with timber verandah posts and native garden"></div>
  <span class="photo__label" style="left:380px;top:678px">Bellintary</span>

  <div class="brand" style="left:145px;top:292px;width:150px;height:90px">
    <span class="brand__name" style="font-size:26px">Capestay</span>
    <span class="brand__tag">south west coast holiday homes</span>
  </div>

  <div class="contact-panel">
    <div class="property-list">
      <div class="property-list__item"><div class="property-list__name">Wattles Retreat</div><div class="property-list__meta">sleeps 12 <small style="font-size:7px">(+ little ones)</small> | <a href="#">www.lodgio.com.au/55841</a></div></div>
      <div class="property-list__item"><div class="property-list__name">Emberlight Retreat</div><div class="property-list__meta">sleeps 8 | <a href="#">www.lodgio.com.au/61673</a></div></div>
      <div class="property-list__item"><div class="property-list__name">Quokkas Corner</div><div class="property-list__meta">sleeps 12 | <a href="#">www.lodgio.com.au/66777</a></div></div>
      <div class="property-list__item"><div class="property-list__name">Bellintary</div><div class="property-list__meta">sleeps 10 | <a href="#">www.lodgio.com.au/93104</a></div></div>
      <div class="property-list__item"><div class="property-list__name">The Glade Retreat</div><div class="property-list__meta">sleeps 8 | <a href="#">www.lodgio.com.au/135790</a></div></div>
      <div class="property-list__item"><div class="property-list__name">Ferncliff Studio</div><div class="property-list__meta">sleeps 4 | <a href="#">www.lodgio.com.au/147300</a></div></div>
    </div>
    <div class="contacts">
      <div class="contacts__brand">Capestay</div>
      <div class="contacts__tag">south west coast holiday homes</div>
      <div class="contacts__person">Kate Marlow</div>
      <div class="contacts__phone"><b>M:</b> 0400 111 222</div>
      <div class="contacts__person">Peter Lazaridis</div>
      <div class="contacts__phone"><b>M:</b> 0400 333 444</div>
    </div>
    <div class="contacts__email"><b>E:</b> capestaysouthwest@mailbox.com</div>
    <p class="contacts__note">All our properties are on rural bush locations, but close to all the amenities of the Tarrabellup township and major wineries in the area.</p>
  </div>
</section>

<section class="flyer flyer--back">
  <div class="photo" style="left:0;top:0;width:212px;height:183px;background:radial-gradient(circle at 45% 45%,#6a3a5a,#7a8a3a 55%,#4a6a1a)" role="img" aria-label="Bunch of red and green wine grapes on the vine"></div>
  <div class="photo" style="left:218px;top:0;width:218px;height:183px;background:linear-gradient(180deg,#3f5a2a,#8a8a5a 55%,#a89a6a)" role="img" aria-label="Kangaroos standing in a grassy bush clearing"></div>
  <div class="brand" style="left:146px;top:66px;width:140px;height:84px">
    <span class="brand__name" style="font-size:24px">Capestay</span>
    <span class="brand__tag">south west coast holiday homes</span>
  </div>

  <div class="about">
    <h2 class="about__title">ABOUT OUR HOUSES</h2>

    <article class="house">
      <h3 class="house__name">Wattles Retreat</h3>
      <p class="house__meta">sleeps 12 <small>(+ little ones)</small> | <span class="url">www.lodgio.com.au/55841</span></p>
      <p class="house__text">Fantastic stone and iron house ideal for families. So peaceful and quiet you won't want to go home. Wattles Retreat is so different from anything else on offer in the South West. It is a fabulous stone and iron family home with two huge lounge areas (one upstairs) with the enormous kitchen/lounge dining area downstairs being over 100m². With 6 bedrooms (10 beds) and 3 bathrooms it's big enough for large groups, friends or families. Pet friendly.</p>
    </article>

    <article class="house">
      <h3 class="house__name">Emberlight Retreat</h3>
      <p class="house__meta">sleeps 8 | <span class="url">www.lodgio.com.au/61673</span></p>
      <p class="house__text">Superbly quiet 5 acre bush location. No neighbours in view or ear shot. The property is only 10 mins to Tarrabellup for shopping, major wineries are only 5-10 mins away. There are lots of walk trails that any afternoon will delight the kids, with kangaroos everywhere to be seen. With 3 bedrooms (5 beds), 2 bathrooms and a 3m wide verandahs wrapping around the front and sides of the house, and opening out onto a small patch of lawn where the kids can play. Pet friendly.</p>
    </article>

    <article class="house">
      <h3 class="house__name">Quokkas Corner</h3>
      <p class="house__meta">sleeps 12 | <span class="url">www.lodgio.com.au/66777</span></p>
      <p class="house__text">Quokkas Corner is a fantastic holiday home, only 10 mins to Tarrabellup and the beaches, but nestled on 5 acres in a lovely quiet location. It is ideal for extended family groups. Close to all the major attractions, beaches wineries and several art galleries nearby. With 6 bedrooms (9 beds) and 3 bathrooms there is plenty of room for the extended family and don't forget the family pet!</p>
    </article>

    <article class="house">
      <h3 class="house__name">Bellintary</h3>
      <p class="house__meta">sleeps 10 | <span class="url">www.lodgio.com.au/93104</span></p>
      <p class="house__text">Bellintary…or 'rest easy' has all you need for a relaxing and fun filled holiday. The quiet location at the end of a cul de sac is very secluded with no neighbours to be seen. Your relaxing time, starts when you first sit on the verandah and watch the birds and kangaroos. Nestled on 6 acres this beautiful house has 4 bedrooms (6 beds) and 2 bathrooms. Pet friendly.</p>
    </article>

    <article class="house">
      <h3 class="house__name">The Glade Retreat</h3>
      <p class="house__meta">sleeps 8 | <span class="url">www.lodgio.com.au/135790</span></p>
      <p class="house__text">This fabulous home is set on 3 acres with a relaxed Bali style layout with all the bedrooms opening out onto the front deck. The fantastic decked areas both front and back allow you to relax in the bush setting and listen to birds. With 4 huge bedrooms (2 with ensuite, 7 beds total) and 3 bathrooms the Glade Retreat will be a great getaway for you and your family. Pet friendly.</p>
    </article>

    <article class="house">
      <h3 class="house__name">Ferncliff Studio</h3>
      <p class="house__meta">sleeps 4 | <span class="url">www.lodgio.com.au/147300</span></p>
      <p class="house__text">Ferncliff Studio is a beautiful, rustic 2 bedroom (2 beds) cottage set amongst 30 acres of parklands and beautiful stands of marri bushland. It is very secluded and has lovely views over adjoining vineyards. The bedrooms are all beautifully decorated and beds are fitted with 500 thread Egyptian cotton sheets for that little bit of luxury.</p>
    </article>
  </div>

  <footer class="back-footer">
    <p class="back-footer__note">All houses have open fires/wood burners for that cosy warmth in winter.</p>
    <div class="back-footer__brand">Capestay</div>
  </footer>
</section>

</body>
</html>
```